Online eyewear company needs a couple Sign-In and Product Review page designs

We sell prescription glasses starting at $99 with Free Shipping. We have over 300 different styles and colors.Our website is under construction and we need an amazing Sign-In and Product Review Pages to help finish things off. Our brand is called VESKA and our website is called VESKAEYEWEAR.COM.

We need 5 simple sign-in and product review pages to help finish our website. Sample pages attached

We need the pages to go in order

Quick Checkout review
Sign-In
Prescription
Shipping & Payment
Final Review

Target Market(s)

20-50 that wears glasses

Industry/Entity Type

Eyewear

Colors
ffffff
919191
eaeaea
d3d3d3
dddddd
b7b7b7
000000
3176b5

Requirements
Must have
• Simple, creative, original. Must not be exactly like the photos attached. They're just templete of our casual, simple style.
• We need the pages to go in order
• Quick Checkout review
• Sign-In
• Prescription
• Shipping & Payment
• Final Review
Should not have
• Must not look exactly like the photos attached.

```html
<!DOCTYPE html>
<html lang="en">
<head>
<meta charset="utf-8">
<title>VESKA – Cart</title>
<link rel="stylesheet" href="https://fonts.googleapis.com/css2?family=Montserrat:wght@400;500;600;700&family=Lato:wght@400;700&display=swap">
<style>
  :root {
    --white: #ffffff;
    --black: #000000;
    --ink: #1a1a1a;
    --text: #333333;
    --muted: #919191;
    --line: #eaeaea;
    --line-dark: #d3d3d3;
    --soft: #dddddd;
    --tile: #f3f4f6;
    --band: #ececec;
    --accent: #c4007a;
    --footer: #2b2b2b;
    --footer-text: #d6d6d6;
  }
  * { box-sizing: border-box; margin: 0; padding: 0; }
  html, body { width: 1200px; height: 2575px; overflow: hidden; }
  body {
    position: relative;
    background: var(--white);
    font-family: "Montserrat", Arial, sans-serif;
    color: var(--text);
  }
  .abs { position: absolute; }
  a { color: inherit; text-decoration: none; }

  /* Top promo bar */
  .promo-bar {
    left: 0; top: 0; width: 1200px; height: 48px;
    background: var(--band);
    font-size: 13px; letter-spacing: .3px; color: var(--ink);
    display: flex; align-items: center; justify-content: center;
  }

  /* Header */
  .site-header { left: 0; top: 48px; width: 1200px; height: 79px; border-bottom: 1px solid var(--line); }
  .brand { left: 103px; top: 20px; font-size: 28px; font-weight: 400; letter-spacing: 5px; color: var(--ink); }
  .main-nav { left: 374px; top: 28px; display: flex; gap: 29px; font-size: 16px; font-weight: 600; color: #333; }
  .util-nav { left: 862px; top: 30px; display: flex; align-items: center; font-size: 14px; color: #555; letter-spacing: .4px; }
  .util-nav .sep { margin: 0 11px; color: #999; }
  .util-nav .search { display: flex; align-items: center; gap: 6px; }
  .util-nav .signin { margin-left: 34px; }
  .cart-btn {
    left: 1136px; top: 16px; width: 56px; height: 56px; border-radius: 50%;
    background: var(--white); box-shadow: 0 2px 8px rgba(0,0,0,.22);
    display: flex; align-items: center; justify-content: center;
  }
  .cart-count {
    left: 1126px; top: 8px; width: 24px; height: 24px; border-radius: 50%;
    background: var(--accent); color: var(--white); font-size: 13px; font-weight: 600;
    display: flex; align-items: center; justify-content: center;
  }

  /* Try-on banner */
  .tryon-banner {
    left: 0; top: 127px; width: 1200px; height: 268px;
    background: radial-gradient(ellipse at 50% 40%, #fbfbfb 0%, #f1f1f1 55%, #e6e6e6 100%);
    text-align: center;
  }
  .tryon-title { position: absolute; left: 0; right: 0; top: 57px; font-size: 29px; font-weight: 500; color: var(--ink); letter-spacing: .3px; }
  .btn-dark {
    background: var(--black); color: var(--white); font-weight: 600;
    display: flex; align-items: center; justify-content: center;
  }
  .tryon-btn { position: absolute; left: 481px; top: 113px; width: 238px; height: 52px; font-size: 16px; }
  .tryon-note { position: absolute; left: 0; right: 0; top: 185px; font-size: 17px; color: #333; letter-spacing: .3px; }

  /* Installment note */
  .installments {
    left: 227px; top: 486px; width: 746px; height: 62px;
    border: 1.5px solid #555;
    display: flex; align-items: center; justify-content: center;
    font-size: 20px; color: var(--ink);
  }

  /* Cart table */
  .cart-head { left: 103px; top: 623px; width: 994px; height: 53px; border-top: 1px solid var(--line); font-size: 17px; color: #444; }
  .cart-head span { position: absolute; top: 16px; }
  .divider { left: 103px; width: 994px; height: 1px; background: var(--line); }

  .product-photo { width: 175px; height: 175px; background: radial-gradient(ellipse at 50% 50%, #d0d0d0 0%, #ececec 40%, var(--tile) 70%); }
  .item-name { font-size: 17px; color: #333; }
  .item-sku { font-size: 17px; color: #333; }
  .item-remove { font-size: 17px; color: #333; display: flex; align-items: center; gap: 10px; }
  .item-price, .item-total { font-size: 17px; color: #333; }
  .qty {
    width: 67px; height: 40px; border: 1px solid var(--line-dark); border-radius: 3px;
    font-size: 16px; color: #333; padding-left: 14px; display: flex; align-items: center;
  }
  .qty svg { position: absolute; right: 8px; top: 8px; }

  /* Summary */
  .side-link { font-size: 16px; color: var(--ink); display: flex; align-items: center; gap: 14px; }
  .secure-badge {
    left: 103px; top: 1342px; width: 216px; height: 62px;
    border: 1.5px solid var(--line-dark); border-radius: 6px; background: #fafafa;
  }
  .secure-badge .shield { position: absolute; left: 6px; top: 3px; }
  .sum-label { left: 716px; font-size: 16px; color: var(--ink); }
  .sum-value { left: 982px; font-size: 16px; color: var(--ink); }
  .underline { text-decoration: underline; text-underline-offset: 4px; }
  .total-label { left: 716px; top: 1351px; font-size: 23px; color: var(--ink); }
  .total-value { left: 982px; top: 1351px; font-size: 23px; font-weight: 500; color: var(--ink); }
  .checkout-btn { left: 716px; top: 1415px; width: 381px; height: 53px; font-size: 22px; font-weight: 500; gap: 14px; }

  .continue { left: 0; width: 1200px; text-align: center; color: var(--ink); }
  .continue-q { top: 1558px; font-size: 21px; }
  .continue-link { top: 1602px; font-size: 20px; font-weight: 700; }

  /* Recommendations */
  .rec-title { left: 0; top: 1724px; width: 1200px; text-align: center; font-size: 35px; font-weight: 400; letter-spacing: 1.5px; color: var(--black); }
  .rec-card { top: 1797px; width: 235px; height: 237px; background: var(--tile); text-align: center; }
  .rec-photo { position: absolute; left: 25px; top: 45px; width: 185px; height: 90px; border-radius: 4px; }
  .rec-name { position: absolute; left: 0; right: 0; top: 150px; font-size: 20px; color: var(--ink); }
  .rec-price { position: absolute; left: 0; right: 0; top: 182px; font-size: 24px; color: var(--ink); }

  /* Footer */
  .site-footer {
    left: 0; top: 2129px; width: 1200px; height: 446px;
    background: linear-gradient(180deg, #4a4a4a 0%, #333333 45%, #262626 100%);
  }
  .footer-brand { left: 110px; top: 68px; font-size: 52px; font-weight: 400; letter-spacing: 9px; color: var(--white); }
  .footer-col { top: 75px; font-family: "Lato", Arial, sans-serif; }
  .footer-col h4 { font-size: 20px; font-weight: 700; color: var(--white); margin-bottom: 12px; letter-spacing: -.2px; }
  .footer-col li { list-style: none; font-size: 17px; color: var(--footer-text); line-height: 31px; }
  .footer-rule { top: 2488px; height: 1px; background: #7a7a7a; }
  .social { top: 2478px; width: 20px; height: 20px; border-radius: 50%; background: var(--white); }
  .copyright { left: 0; top: 2524px; width: 1200px; text-align: center; font-family: "Lato", Arial, sans-serif; font-size: 13px; color: #bdbdbd; }
</style>
</head>
<body>

  <div class="abs promo-bar">FREE SHIPPING IN CONTINENTAL US</div>

  <header class="abs site-header">
    <div class="abs brand">VESKA</div>
    <nav class="abs main-nav"><a>EYEGLASSES</a><a>ORDER LENSES</a></nav>
    <div class="abs util-nav">
      <span class="search">
        <svg width="17" height="17" viewBox="0 0 17 17"><circle cx="7" cy="7" r="5.5" fill="none" stroke="#888" stroke-width="2"/><line x1="11" y1="11" x2="16" y2="16" stroke="#888" stroke-width="2.4"/></svg>
        SEARCH
      </span>
      <span class="sep">|</span>
      <span>HELP</span>
      <span class="signin">SIGN IN</span>
    </div>
  </header>
  <div class="abs cart-btn">
    <svg width="28" height="24" viewBox="0 0 28 24"><path d="M2 9h24l-3 13H5z" fill="#111"/><path d="M8 9l6-7 6 7" fill="none" stroke="#111" stroke-width="2.2"/><circle cx="10" cy="15" r="1.5" fill="#fff"/><circle cx="18" cy="15" r="1.5" fill="#fff"/></svg>
  </div>
  <div class="abs cart-count">2</div>

  <section class="abs tryon-banner">
    <h1 class="tryon-title">You have 2 Home Try-On frame in your cart</h1>
    <a class="tryon-btn btn-dark">Check out (it's free)</a>
    <p class="tryon-note">Free standard shipping and free returns on all orders</p>
  </section>

  <div class="abs installments">You can make 3 interest-free payments of $80 with Paylo at checkout</div>

  <div class="abs cart-head">
    <span style="left:34px">Product</span>
    <span style="left:544px">Price</span>
    <span style="left:735px">Qty</span>
    <span style="left:879px">Total</span>
  </div>

  <!-- Item 1 -->
  <div class="abs product-photo" style="left:103px;top:721px" role="img" aria-label="Tortoiseshell rectangular eyeglass frame"></div>
  <div class="abs item-name" style="left:333px;top:758px">Adipiscing sem</div>
  <div class="abs item-sku" style="left:333px;top:796px">SKU: 003</div>
  <div class="abs item-remove" style="left:333px;top:835px">
    <svg width="13" height="16" viewBox="0 0 13 16"><path d="M1 3h11M4.5 3V1.5h4V3M2.5 3l.8 12h6.4l.8-12" fill="none" stroke="#333" stroke-width="1.3"/><path d="M5 6v6M8 6v6" stroke="#333" stroke-width="1.1"/></svg>
    Remove
  </div>
  <div class="abs item-price" style="left:647px;top:758px">$150.00</div>
  <div class="abs qty" style="left:824px;top:750px">1
    <svg width="10" height="22" viewBox="0 0 10 22"><path d="M2 6l3-3 3 3M2 16l3 3 3-3" fill="none" stroke="#888" stroke-width="1.2"/></svg>
  </div>
  <div class="abs item-total" style="left:982px;top:758px">$150.00</div>

  <div class="abs divider" style="top:941px"></div>

  <!-- Item 2 -->
  <div class="abs product-photo" style="left:103px;top:985px" role="img" aria-label="Black browline eyeglass frame"></div>
  <div class="abs item-name" style="left:333px;top:1022px">Dapibus In Viverra</div>
  <div class="abs item-sku" style="left:333px;top:1060px">SKU: 018</div>
  <div class="abs item-remove" style="left:333px;top:1099px">
    <svg width="13" height="16" viewBox="0 0 13 16"><path d="M1 3h11M4.5 3V1.5h4V3M2.5 3l.8 12h6.4l.8-12" fill="none" stroke="#333" stroke-width="1.3"/><path d="M5 6v6M8 6v6" stroke="#333" stroke-width="1.1"/></svg>
    Remove
  </div>
  <div class="abs item-price" style="left:647px;top:1022px">$120.00</div>
  <div class="abs qty" style="left:824px;top:1014px">1
    <svg width="10" height="22" viewBox="0 0 10 22"><path d="M2 6l3-3 3 3M2 16l3 3 3-3" fill="none" stroke="#888" stroke-width="1.2"/></svg>
  </div>
  <div class="abs item-total" style="left:982px;top:1022px">$120.00</div>

  <div class="abs divider" style="top:1205px"></div>

  <!-- Summary -->
  <div class="abs side-link" style="left:107px;top:1238px">
    <svg width="16" height="16" viewBox="0 0 16 16"><path d="M1 1h7l7 7-7 7-7-7z" fill="#111"/><circle cx="4.5" cy="4.5" r="1.4" fill="#fff"/></svg>
    Enter a promo code
  </div>
  <div class="abs side-link" style="left:107px;top:1281px">
    <svg width="18" height="16" viewBox="0 0 18 16"><rect x="1" y="3" width="12" height="12" fill="none" stroke="#111" stroke-width="1.5"/><path d="M7 10l1-3 8-6 2 2-8 6z" fill="#111"/></svg>
    Add a note
  </div>
  <div class="abs secure-badge">
    <svg class="shield" width="52" height="56" viewBox="0 0 52 56"><path d="M4 6l22-4 22 4v22c0 14-12 22-22 26C16 50 4 42 4 28z" fill="#7cbf3a"/><path d="M15 28l8 8 15-16" fill="none" stroke="#fff" stroke-width="5"/></svg>
  </div>

  <div class="abs sum-label" style="top:1238px">Subtotal</div>
  <div class="abs sum-value" style="top:1238px">$270.00</div>
  <div class="abs sum-label underline" style="top:1281px">Estimate Shipping</div>
  <div class="abs divider" style="left:716px;width:381px;top:1327px"></div>
  <div class="abs total-label">Total</div>
  <div class="abs total-value">$270.00</div>
  <a class="abs checkout-btn btn-dark">
    <svg width="15" height="18" viewBox="0 0 15 18"><path d="M3.5 8V5a4 4 0 018 0v3" fill="none" stroke="#fff" stroke-width="2"/><rect x="1" y="8" width="13" height="10" rx="1" fill="#fff"/></svg>
    Checkout
  </a>

  <p class="abs continue continue-q">Still want to continue shopping?</p>
  <a class="abs continue continue-link"><span class="underline">Shop Frames</span></a>

  <!-- Recommended -->
  <h2 class="abs rec-title">RECOMMENDED</h2>
  <div class="abs rec-card" style="left:103px">
    <div class="rec-photo" role="img" aria-label="Clear mint eyeglass frame" style="background:radial-gradient(ellipse,#cfdcd8 0%,var(--tile) 70%)"></div>
    <div class="rec-name">Amari</div><div class="rec-price">$99.00</div>
  </div>
  <div class="abs rec-card" style="left:355px">
    <div class="rec-photo" role="img" aria-label="Blush pink round eyeglass frame" style="background:radial-gradient(ellipse,#e2bfb1 0%,var(--tile) 70%)"></div>
    <div class="rec-name">Zoe</div><div class="rec-price">$99.00</div>
  </div>
  <div class="abs rec-card" style="left:609px">
    <div class="rec-photo" role="img" aria-label="Coral transparent eyeglass frame" style="background:radial-gradient(ellipse,#ecbcae 0%,var(--tile) 70%)"></div>
    <div class="rec-name">Amari</div><div class="rec-price">$99.00</div>
  </div>
  <div class="abs rec-card" style="left:862px">
    <div class="rec-photo" role="img" aria-label="Grey marbled eyeglass frame" style="background:radial-gradient(ellipse,#9aa09c 0%,var(--tile) 70%)"></div>
    <div class="rec-name">Ari</div><div class="rec-price">$99.00</div>
  </div>

  <!-- Footer -->
  <footer class="abs site-footer" role="img" aria-label="Footer backdrop with faint clear eyeglass frame">
    <div class="abs footer-brand">VESKA</div>
    <div class="abs footer-col" style="left:402px">
      <h4>PRODUCTS</h4>
      <ul><li>Men's Frames</li><li>Women's Frames</li><li>New Arrivals</li><li>Best Sellers</li><li>Featured Frames</li></ul>
    </div>
    <div class="abs footer-col" style="left:654px">
      <h4>ORDER</h4>
      <ul><li>Single Vision Lenses</li><li>Blue Light Blocking</li><li>Computer Lenses</li><li>High Index Lenses</li><li>Transition Lenses</li><li>Reading Lenses</li></ul>
    </div>
    <div class="abs footer-col" style="left:908px">
      <h4>INFORMATION</h4>
      <ul><li>Track Order</li><li>About Us</li><li>FAQ</li><li>Contact Us</li></ul>
    </div>
  </footer>
  <div class="abs footer-rule" style="left:107px;width:448px"></div>
  <div class="abs footer-rule" style="left:648px;width:443px"></div>
  <div class="abs social" style="left:565px"></div>
  <div class="abs social" style="left:607px"></div>
  <p class="abs copyright">© 2019 Veska. All Right Reserved. Privacy Policy | Terms of Use</p>

</body>
</html>
```